Lantern Hill Publicity is a new boutique Press Office with a small roster of well-chosen clients across an array of disciplines; from Art and Technology to Restaurants and Fashion. Based in Greenpoint Brooklyn, Lantern Hill Publicity achieves outstanding results through hard work, tenacity, efficiency and a sense of humor. We need a simple, versatile and classic design. We would like each side of the card to be white text on a black background.

Boutique

```html
<!DOCTYPE html>
<html lang="en">
<head>
<meta charset="utf-8">
<title>Lantern Hill Publicity — Business Card</title>
<link rel="stylesheet" href="https://fonts.googleapis.com/css2?family=Playfair+Display:wght@400;700&display=swap">
<style>
  :root {
    --backdrop: #e9e6e1;
    --card: #141416;
    --ink: #ffffff;
    --ink-soft: #d9d9d9;
    --rule: #8a8a8a;
  }
  * { margin: 0; padding: 0; box-sizing: border-box; }
  html, body {
    width: 1200px; height: 891px; overflow: hidden;
    background: var(--backdrop);
    font-family: "Playfair Display", Georgia, serif;
    color: var(--ink);
  }
  .sheet {
    position: relative; width: 1200px; height: 891px;
    display: flex; align-items: center; justify-content: center; gap: 50px;
  }
  .card {
    position: relative; width: 525px; height: 300px;
    background: var(--card);
    box-shadow: 0 10px 30px rgba(0,0,0,.18);
  }
  .wordmark { text-align: center; font-weight: 400; }
  .wordmark__name {
    display: block; font-size: 25px; letter-spacing: .22em; line-height: 1;
  }
  .wordmark__sub {
    display: block; font-size: 10px; letter-spacing: .65em; margin-top: 8px; color: var(--ink);
  }
  .card--front { display: flex; align-items: center; justify-content: center; }
  .card--back .wordmark { position: absolute; left: 40px; top: 48px; text-align: left; }
  .card--back .wordmark__name { font-size: 22px; }
  .contact { position: absolute; right: 36px; bottom: 30px; width: 230px; }
  .contact__name { font-size: 24px; font-weight: 700; line-height: 1.1; }
  .contact__role { font-size: 11px; color: var(--ink-soft); margin: 3px 0 10px; letter-spacing: .04em; }
  .contact__rule { border: 0; border-top: 1px solid var(--rule); margin: 6px 0; }
  .contact__line { font-size: 11px; line-height: 1.6; color: var(--ink-soft); }
</style>
</head>
<body>
<main class="sheet">
  <section class="card card--front" aria-label="Card front">
    <div class="wordmark">
      <span class="wordmark__name">LANTERN HILL</span>
      <span class="wordmark__sub">PUBLICITY</span>
    </div>
  </section>

  <section class="card card--back" aria-label="Card back">
    <div class="wordmark">
      <span class="wordmark__name">LANTERN HILL</span>
      <span class="wordmark__sub">PUBLICITY</span>
    </div>
    <div class="contact">
      <p class="contact__name">Clara Voss</p>
      <p class="contact__role">Director</p>
      <p class="contact__line">T. +1 718 555 0142</p>
      <p class="contact__line">E. hello@lanternhillpr.com</p>
      <p class="contact__line">W. www.lanternhillpr.com</p>
      <hr class="contact__rule">
      <p class="contact__line">88 Franklin Street</p>
      <p class="contact__line">Greenpoint, Brooklyn NY</p>
      <hr class="contact__rule">
    </div>
  </section>
</main>
</body>
</html>
```